New business card for UK roofing company

We are Brindmore Roofing and we need a business card design for our staff.

We offer the following services:

- New roofs
- General roof repairs
- Drone surveys
- Single ply roofing
- Steel cladding
- Asbestos removal
- Electronic leak detection

I have attached our logo. I have also attached example branding printed to our vans. The business card should fit in with the style of our branding.

The business card should have the following information;

Address:
Unit 17c Wendlecroft Farm
Wendlecroft Lane
Hatchington
CM4 9QD

Telephone: 020 7946 0372
24 Hour: 0800 612 4479

Email: ray@brindmoreroofing.example
Mobile: 07700981234
Name: Ray Tunstead
Website: www.brindmoreroofing.example

The business card will be printed in Spot UV, see here: https://www.kestaprint.example/business-cards/spot-uv/

If you need anymore info, please let me know,

```html
<!DOCTYPE html>
<html lang="en">
<head>
<meta charset="utf-8">
<title>Brindmore Roofing – Business Card</title>
<link href="https://fonts.googleapis.com/css2?family=Lato:wght@400;700;900&display=swap" rel="stylesheet">
<style>
  :root {
    --navy: #144a7d;
    --navy-deep: #0f3d69;
    --cyan: #0aa9dd;
    --white: #ffffff;
    --backdrop: #3a3a3a;
  }
  * { margin: 0; padding: 0; box-sizing: border-box; }
  html, body { width: 1200px; height: 689px; overflow: hidden; }
  body {
    background: var(--backdrop);
    font-family: "Lato", sans-serif;
    position: relative;
  }
  .card {
    position: absolute;
    top: 170px;
    width: 540px;
    height: 349px;
    border-radius: 22px;
    overflow: hidden;
    background: var(--navy);
  }
  .card--contact { left: 40px; }
  .card--services { left: 620px; }
  .card__shape { position: absolute; inset: 0; width: 100%; height: 100%; }

  /* contact side */
  .holder {
    position: absolute; right: 28px; top: 24px; text-align: right;
  }
  .holder__name {
    color: var(--cyan); font-weight: 900; font-size: 25px; letter-spacing: 0.5px; line-height: 1.1;
  }
  .holder__email { color: var(--white); font-size: 12px; margin-top: 3px; }

  .contact-list {
    position: absolute; left: 28px; top: 98px; list-style: none;
    color: var(--white); font-size: 13px; line-height: 1.35;
  }
  .contact-list li { display: flex; align-items: flex-start; gap: 10px; margin-bottom: 6px; }
  .contact-list .icon { width: 14px; height: 14px; flex: none; margin-top: 2px; }
  .contact-list strong { font-weight: 700; }

  .wordmark {
    font-weight: 900; color: var(--cyan); letter-spacing: -0.5px;
    display: flex; align-items: center; gap: 8px; line-height: 1;
  }
  .wordmark__dot { border-radius: 50%; background: var(--cyan); flex: none; }
  .card--contact .wordmark { position: absolute; left: 30px; bottom: 32px; font-size: 30px; }
  .card--contact .wordmark__dot { width: 20px; height: 20px; }

  /* services side */
  .card--services .wordmark {
    position: absolute; left: 0; right: 0; top: 100px; justify-content: center; font-size: 46px;
  }
  .card--services .wordmark__dot { width: 30px; height: 30px; }
  .services {
    position: absolute; right: 34px; bottom: 40px; width: 380px;
    text-align: center; color: var(--navy-deep);
    font-size: 11.5px; font-weight: 700; text-transform: uppercase; line-height: 1.55;
  }
  .services .sep { color: var(--cyan); }
</style>
</head>
<body>

<section class="card card--contact" aria-label="Business card, contact side">
  <svg class="card__shape" viewBox="0 0 540 349" aria-hidden="true">
    <rect width="540" height="349" fill="var(--navy)"/>
    <path d="M0 272 Q 250 252 540 152 L540 349 L0 349 Z" fill="var(--white)"/>
    <path d="M0 263 Q 250 243 540 143" fill="none" stroke="var(--cyan)" stroke-width="7"/>
    <circle cx="482" cy="202" r="124" fill="var(--white)"/>
    <circle cx="482" cy="202" r="110" fill="var(--cyan)"/>
  </svg>

  <div class="holder">
    <div class="holder__name">RAY TUNSTEAD</div>
    <div class="holder__email">ray@brindmoreroofing.example</div>
  </div>

  <ul class="contact-list">
    <li>
      <svg class="icon" viewBox="0 0 14 14" aria-hidden="true"><path d="M7 1a4 4 0 0 0-4 4c0 3 4 8 4 8s4-5 4-8a4 4 0 0 0-4-4z" fill="var(--cyan)"/><circle cx="7" cy="5" r="1.5" fill="var(--navy)"/></svg>
      <span>Unit 17c Wendlecroft Farm<br>Wendlecroft Lane, Hatchington, CM4 9QD</span>
    </li>
    <li>
      <svg class="icon" viewBox="0 0 14 14" aria-hidden="true"><path d="M3 1l2 0 1 3-1.5 1a7 7 0 0 0 3.5 3.5L9 7l3 1v2a2 2 0 0 1-2 2A9 9 0 0 1 1 3a2 2 0 0 1 2-2z" fill="var(--cyan)"/></svg>
      <span><strong>020 7946 0372</strong><br><strong>0800 612 4479 (24Hr)</strong></span>
    </li>
    <li>
      <svg class="icon" viewBox="0 0 14 14" aria-hidden="true"><rect x="3.5" y="1" width="7" height="12" rx="1.5" fill="none" stroke="var(--cyan)" stroke-width="1.5"/><circle cx="7" cy="11" r="0.8" fill="var(--cyan)"/></svg>
      <span>07700 981234</span>
    </li>
    <li>
      <svg class="icon" viewBox="0 0 14 14" aria-hidden="true"><circle cx="7" cy="7" r="5.5" fill="none" stroke="var(--cyan)" stroke-width="1.4"/><path d="M1.5 7h11M7 1.5c-3 3.5-3 7.5 0 11M7 1.5c3 3.5 3 7.5 0 11" fill="none" stroke="var(--cyan)" stroke-width="1"/></svg>
      <span>brindmoreroofing.example</span>
    </li>
  </ul>

  <div class="wordmark"><span class="wordmark__dot"></span>brindmoreroofing</div>
</section>

<section class="card card--services" aria-label="Business card, services side">
  <svg class="card__shape" viewBox="0 0 540 349" aria-hidden="true">
    <rect width="540" height="349" fill="var(--navy)"/>
    <path d="M0 349 Q 150 200 540 148 L540 349 Z" fill="var(--white)"/>
    <path d="M10 349 Q 155 190 540 135" fill="none" stroke="var(--cyan)" stroke-width="7"/>
  </svg>

  <div class="wordmark"><span class="wordmark__dot"></span>brindmoreroofing</div>

  <p class="services">
    New Roofs <span class="sep">•</span> General Roof Repairs <span class="sep">•</span> Drone Surveys<br>
    Single Ply Roofing <span class="sep">•</span> Steel Cladding <span class="sep">•</span> Asbestos Removal<br>
    Electronic Leak Detection
  </p>
</section>

</body>
</html>
```